Design Bag for Kelwin Crisp Co.

Create a full front and back design for Kelwin Crisp Co. with area for nutrition label. I would like a to take Kelwin Crisp Co. into the 21st century with a Hawaiian vibe. I would like a window about 2 inches from bottom to see the jerky chip.
Must Haves:
Hawai'i's Premium Beef Jerky Chips
100% Grass Fed Hawai'i Beef No Antibiotics No Growth Hormones
Made Exclusively In Hawaii
Extra Thin Extra Crispy

Target Market(s)

18-75 who doesnt like jerky

Requirements
Must have
• Hawai'i's Premium Beef Jerky Chips
Extra Thin, Extra Crispy
Color
Window
Area for the flavor. Start with TERIYAKI

```html
<!DOCTYPE html>
<html lang="en">
<head>
<meta charset="utf-8">
<title>Kelwin Crisp Co. – Beef Jerky Chips Bag</title>
<link href="https://fonts.googleapis.com/css2?family=Bebas+Neue&family=Kaushan+Script&family=Roboto+Condensed:wght@400;700&family=Roboto:wght@400;700&display=swap" rel="stylesheet">
<style>
  :root{
    --yellow:#f2b705;
    --yellow-deep:#e6a000;
    --amber:#d98e0c;
    --brown:#9c5426;
    --brown-dark:#7e3f1a;
    --red:#d0202a;
    --ink:#141414;
    --white:#ffffff;
    --cream:#f6e3b4;
  }
  *{box-sizing:border-box;margin:0;padding:0}
  html,body{width:1200px;height:1001px;overflow:hidden;background:var(--white)}
  .stage{position:relative;width:1200px;height:1001px}
  .panel{position:absolute;top:166px;width:520px;height:668px;overflow:hidden;
    background:radial-gradient(ellipse at 50% 25%,var(--yellow) 0%,var(--yellow-deep) 60%,var(--amber) 100%);
    box-shadow:0 14px 24px rgba(0,0,0,.18)}
  .panel--front{left:50px}
  .panel--back{left:630px}
  .abs{position:absolute}

  .tab{position:absolute;top:126px;width:135px;height:69px}
  .tab svg{position:absolute;inset:0}
  .tab__text{position:absolute;inset:0;display:flex;flex-direction:column;justify-content:center;
    font-family:'Bebas Neue',sans-serif;font-size:27px;line-height:.88;color:var(--yellow)}
  .tab--left{left:0}
  .tab--left .tab__text{padding-left:38px}
  .tab--right{right:0}
  .tab--right .tab__text{padding-left:34px}

  .brand{position:absolute;left:111px;top:96px;width:300px;text-align:center;
    font-family:'Bebas Neue',sans-serif;font-size:52px;line-height:.95;color:var(--brown-dark)}

  .script{font-family:'Kaushan Script',cursive;color:var(--ink);text-align:center;white-space:nowrap}
  .headline{font-family:'Bebas Neue',sans-serif;color:var(--ink);text-align:center;white-space:nowrap;
    -webkit-text-stroke:1px var(--white);paint-order:stroke fill;letter-spacing:.5px}

  .front-script{left:0;width:520px;top:296px;font-size:34px;transform:rotate(-3deg)}
  .front-headline{left:0;width:520px;top:338px;font-size:64px}
  .window{left:38px;top:410px;width:443px;height:117px;background:var(--white);border-radius:16px}

  .band{position:absolute;left:0;right:0;bottom:0;height:124px;background:var(--brown)}
  .flavor{position:absolute;left:167px;bottom:0;width:186px;height:111px;background:var(--red);
    border-radius:12px 12px 0 0;display:flex;align-items:center;justify-content:center}
  .flavor__name{font-family:'Kaushan Script',cursive;font-size:42px;color:var(--yellow);transform:rotate(-4deg) translateY(-14px)}

  .claims{position:absolute;left:34px;top:580px;width:112px;color:var(--white);text-align:center;
    font-family:'Roboto Condensed',sans-serif}
  .claims__main{font-weight:700;font-size:9.5px;line-height:1.25;padding-bottom:4px;border-bottom:1px solid var(--white)}
  .claims__row{display:flex;font-size:9.5px;line-height:1.2;margin-top:4px}
  .claims__row span{flex:1}
  .claims__row span+span{border-left:1px solid var(--white)}

  .origin{position:absolute;left:380px;top:586px;width:100px;color:var(--white);font-family:'Roboto Condensed',sans-serif}
  .origin__weight{font-weight:700;font-size:9.5px;text-align:center;padding-bottom:4px;border-bottom:1px solid var(--white)}
  .origin__made{display:flex;align-items:center;gap:5px;margin-top:6px;font-size:9.5px;line-height:1.2}

  .artwork{left:0;top:105px;width:330px;height:515px;border-radius:0 160px 120px 0;
    background:linear-gradient(160deg,#b97a45 0%,#a4653a 55%,#c9302c 100%);opacity:.9}
  .back-script{left:291px;width:160px;top:48px;font-size:21px;transform:rotate(-3deg)}
  .back-headline{left:246px;width:250px;top:80px;font-size:34px}
  .back-flavor{left:271px;width:200px;top:118px;font-size:32px;color:var(--red);transform:rotate(-3deg)}

  .nutrition{left:280px;top:181px;width:182px;height:306px;background:var(--white);border-radius:5px;
    padding:8px 4px 6px 4px;font-family:'Roboto',sans-serif;color:var(--ink)}
  .nutrition__title{font-weight:700;font-size:20px;line-height:1;margin-left:8px}
  .nutrition__meta{font-size:8px;line-height:1.3;margin-top:3px;padding-bottom:3px;border-bottom:4px solid var(--ink)}
  .nutrition__small{font-size:6px;padding:3px 0;border-bottom:1px solid var(--ink)}
  .nrow{display:flex;justify-content:space-between;font-size:8px;line-height:1;padding:3px 2px;border-bottom:1px solid var(--ink)}
  .nrow--indent{padding-left:10px}
  .nrow--thick{border-bottom:3px solid var(--ink)}
  .nrow--right{justify-content:flex-end}
  .nutrition__foot{font-size:7.5px;line-height:1.15;margin:6px 2px 0 6px}

  .contact{left:300px;top:495px;width:142px;text-align:center;font-family:'Roboto',sans-serif;
    font-size:6.5px;line-height:1.3;color:var(--brown-dark)}
  .code-box{left:301px;top:558px;width:141px;height:73px;background:var(--white)}
</style>
</head>
<body>
<main class="stage">

  <section class="panel panel--front" aria-label="Bag front">
    <div class="tab tab--left">
      <svg viewBox="0 0 135 69" width="135" height="69"><polygon points="0,0 120,0 135,34.5 120,69 0,69" fill="var(--red)"/></svg>
      <div class="tab__text"><span>Extra</span><span>Thin</span></div>
    </div>
    <div class="tab tab--right">
      <svg viewBox="0 0 135 69" width="135" height="69"><polygon points="15,0 135,0 135,69 15,69 0,34.5" fill="var(--red)"/></svg>
      <div class="tab__text"><span>Extra</span><span>Crispy</span></div>
    </div>

    <div class="brand">Kelwin<br>Crisp Co.</div>

    <div class="abs script front-script">Hawai'i's Premium</div>
    <div class="abs headline front-headline">BEEF JERKY CHIPS</div>
    <div class="abs window" aria-label="Clear window showing the jerky chips"></div>

    <div class="band">
      <div class="flavor"><span class="flavor__name">Teriyaki</span></div>
    </div>
    <div class="claims">
      <div class="claims__main">100% GRASS FED<br>HAWAI'I BEEF</div>
      <div class="claims__row"><span>No<br>Antibiotics</span><span>No Growth<br>Hormones</span></div>
    </div>
    <div class="origin">
      <div class="origin__weight">NET WT: 00G</div>
      <div class="origin__made">
        <svg width="20" height="20" viewBox="0 0 20 20" aria-hidden="true">
          <g fill="none" stroke="#fff" stroke-width="1.3">
            <circle cx="10" cy="4.5" r="3.5"/><circle cx="15.2" cy="8.3" r="3.5"/><circle cx="13.2" cy="14.5" r="3.5"/><circle cx="6.8" cy="14.5" r="3.5"/><circle cx="4.8" cy="8.3" r="3.5"/>
          </g>
          <circle cx="10" cy="10" r="2" fill="#fff"/>
        </svg>
        <span>Made Exclusively<br>In Hawaii</span>
      </div>
    </div>
  </section>

  <section class="panel panel--back" aria-label="Bag back">
    <div class="abs artwork" role="img" aria-label="Illustration area: bull mascot in red boxing gloves"></div>

    <div class="abs script back-script">Hawai'i's Premium</div>
    <div class="abs headline back-headline">BEEF JERKY CHIPS</div>
    <div class="abs script back-flavor">Teriyaki</div>

    <div class="abs nutrition" aria-label="Nutrition label area">
      <div class="nutrition__title">Nutrition Facts</div>
      <div class="nutrition__meta">Serving Size oz.<br>Serving Per Container</div>
      <div class="nutrition__small">Amount Per Serving:</div>
      <div class="nrow"><span>Calories</span><span>Calories From Fat&nbsp;&nbsp;&nbsp;&nbsp;</span></div>
      <div class="nrow nrow--right"><span>% Daily value*</span></div>
      <div class="nrow"><span>Total Fat</span><span>%</span></div>
      <div class="nrow nrow--indent"><span>Saturated Fat</span><span>%</span></div>
      <div class="nrow nrow--indent"><span>Trans Fat</span><span></span></div>
      <div class="nrow"><span>Cholesterol</span><span>%</span></div>
      <div class="nrow"><span>Sodium</span><span>%</span></div>
      <div class="nrow"><span>Total Carbohydrate</span><span>%</span></div>
      <div class="nrow nrow--indent"><span>Dietary Fiber</span><span>%</span></div>
      <div class="nrow nrow--indent"><span>Sugars</span><span></span></div>
      <div class="nrow nrow--thick"><span>Protein</span><span></span></div>
      <div class="nutrition__foot">*Percent Daily values are based on a 2000 calorie diet. Your daily values may be higher or lewer depending on you calorie needs.</div>
    </div>

    <div class="abs contact">Company Address<br>Contact Number<br>Email Address<br>Website Address</div>

    <div class="band"></div>
    <div class="abs code-box"></div>
  </section>

</main>
</body>
</html>
```